Everything fresh, everything new

When I take over the practice, I would like to breathe new life into the practice. I want a business card design that catches the eye and brings a breath of fresh air

```html
<!DOCTYPE html>
<html lang="en">
<head>
<meta charset="utf-8">
<title>Praxis Aufwind – Business Card</title>
<link href="https://fonts.googleapis.com/css2?family=Lato:wght@400;700;900&display=swap" rel="stylesheet">
<style>
  :root {
    --page-bg: #d9d4d2;
    --card-bg: #e7e4e6;
    --green-light: #93c266;
    --green-mid: #6da23a;
    --green-deep: #4e891d;
    --text-light: #eef0ea;
    --name-silver: #ece6e8;
    --ink-dark: #2a2a2c;
  }
  * { margin: 0; padding: 0; box-sizing: border-box; }
  html, body {
    width: 1200px; height: 734px; overflow: hidden;
    background: var(--page-bg);
    font-family: "Lato", Arial, sans-serif;
  }
  .business-card {
    position: absolute; left: 20px; top: 35px;
    width: 1160px; height: 664px;
    background: var(--card-bg);
    border-radius: 30px;
    overflow: hidden;
    box-shadow: 0 2px 10px rgba(0,0,0,0.12);
  }
  .green-panel { position: absolute; inset: 0; width: 1160px; height: 664px; }
  .holder-name {
    position: absolute; left: 72px; top: 72px;
    font-size: 52px; font-weight: 900; letter-spacing: 0.5px;
    color: var(--name-silver);
  }
  .holder-role {
    position: absolute; left: 73px; top: 132px;
    font-size: 31px; font-weight: 400; color: var(--text-light);
  }
  .contact-list { position: absolute; left: 70px; top: 292px; list-style: none; }
  .contact-item {
    display: flex; align-items: flex-start;
    font-size: 28px; line-height: 40px; color: var(--text-light);
  }
  .contact-item.phone { font-size: 31px; }
  .contact-item + .contact-item { margin-top: 1px; }
  .contact-item.address { margin-bottom: 10px; }
  .contact-icon { width: 26px; height: 26px; margin: 7px 16px 0 0; flex: none; }
  .brand-lockup {
    position: absolute; left: 690px; top: 452px;
    display: flex; align-items: center; gap: 16px;
  }
  .brand-dot { width: 22px; height: 22px; border-radius: 50%; background: var(--green-deep); }
  .brand-name { font-size: 56px; font-weight: 700; color: var(--ink-dark); letter-spacing: -0.5px; }
</style>
</head>
<body>
  <main class="business-card">
    <svg class="green-panel" viewBox="0 0 1160 664" aria-hidden="true">
      <defs>
        <linearGradient id="panelGradient" x1="0" y1="0" x2="1" y2="0">
          <stop offset="0" stop-color="var(--green-light)"/>
          <stop offset="0.35" stop-color="var(--green-light)"/>
          <stop offset="0.7" stop-color="var(--green-mid)"/>
          <stop offset="1" stop-color="var(--green-deep)"/>
        </linearGradient>
      </defs>
      <path d="M0 0 H780 C860 0 885 100 855 185 C805 325 565 420 505 560 C482 612 486 640 492 664 H0 Z" fill="url(#panelGradient)"/>
    </svg>

    <h1 class="holder-name">JONAS KELLER</h1>
    <p class="holder-role">Founder &amp; CEO</p>

    <ul class="contact-list">
      <li class="contact-item address">
        <svg class="contact-icon" viewBox="0 0 24 24"><path d="M12 2a7 7 0 0 0-7 7c0 5 7 13 7 13s7-8 7-13a7 7 0 0 0-7-7zm0 9.5A2.5 2.5 0 1 1 12 6.5a2.5 2.5 0 0 1 0 5z" fill="currentColor"/></svg>
        <span>Your Address, City<br>State, Country, Zip 1235</span>
      </li>
      <li class="contact-item phone">
        <svg class="contact-icon" viewBox="0 0 24 24"><path d="M6.6 10.8a15 15 0 0 0 6.6 6.6l2.2-2.2a1 1 0 0 1 1-.25 11.4 11.4 0 0 0 3.6.6 1 1 0 0 1 1 1V20a1 1 0 0 1-1 1A17 17 0 0 1 3 4a1 1 0 0 1 1-1h3.5a1 1 0 0 1 1 1c0 1.25.2 2.45.6 3.6a1 1 0 0 1-.25 1z" fill="currentColor"/></svg>
        <span>(123) 456-7890</span>
      </li>
      <li class="contact-item phone">
        <svg class="contact-icon" viewBox="0 0 24 24"><rect x="6" y="2" width="12" height="20" rx="2" fill="none" stroke="currentColor" stroke-width="2"/><circle cx="12" cy="18" r="1.2" fill="currentColor"/></svg>
        <span>(231) 456-7890</span>
      </li>
      <li class="contact-item phone">
        <svg class="contact-icon" viewBox="0 0 24 24"><path d="M7 3h10v5H7z M4 9h16a1 1 0 0 1 1 1v6h-4v5H7v-5H3v-6a1 1 0 0 1 1-1z M9 15v4h6v-4z" fill="currentColor" fill-rule="evenodd"/></svg>
        <span>(231) 456-7890</span>
      </li>
      <li class="contact-item">
        <svg class="contact-icon" viewBox="0 0 24 24"><path d="M3 5h18v14H3z" fill="currentColor"/><path d="M3 5l9 8 9-8" fill="none" stroke="var(--green-mid)" stroke-width="1.6"/></svg>
        <span>info@praxis-aufwind.com</span>
      </li>
      <li class="contact-item">
        <svg class="contact-icon" viewBox="0 0 24 24"><circle cx="12" cy="12" r="9" fill="none" stroke="currentColor" stroke-width="2"/><path d="M3 12h18M12 3c3 3 3 15 0 18M12 3c-3 3-3 15 0 18" fill="none" stroke="currentColor" stroke-width="1.5"/></svg>
        <span>praxis-aufwind.com</span>
      </li>
    </ul>

    <div class="brand-lockup">
      <span class="brand-dot"></span>
      <span class="brand-name">Praxis Aufwind</span>
    </div>
  </main>
</body>
</html>
```